CSLN Banner

We need a design for a pull-up banner (850 x 2000 mm) to promote the Civic Strand Ledger Norm. https://cslnorm.net/en/
The banner action should be to get people to scan a QR code to join a mailing list (add a frame to add the QR code)

Use the website colours and typology https://cslnorm.net/en/
See also brochure for ideas https://cslnorm.net/documents/9/CSLN_brochure_english.pdf

```html
<!DOCTYPE html>
<html lang="en">
<head>
<meta charset="utf-8">
<title>CSLN Pull-up Banner</title>
<link href="https://fonts.googleapis.com/css2?family=Montserrat:wght@500;600;700;800&display=swap" rel="stylesheet">
<style>
  :root {
    --page: #ececec;
    --night: #0b0a1d;
    --ink: #0a0f24;
    --lime: #c3d62f;
    --white: #ffffff;
    --green: #22b96e;
    --teal: #1a94a0;
    --blue: #1166c6;
    --link: #3d8fd6;
    --globe: #1a1d4a;
  }
  html, body {
    margin: 0;
    width: 1200px;
    height: 1200px;
    overflow: hidden;
    background: var(--page);
  }
  .banner {
    position: absolute;
    left: 357px;
    top: 30px;
    width: 486px;
    height: 1140px;
    background: var(--night);
    overflow: hidden;
    font-family: "Montserrat", sans-serif;
    color: var(--white);
    text-align: center;
    box-shadow: 0 4px 14px rgba(0,0,0,.18);
  }
  .banner__header {
    position: absolute;
    left: 0;
    top: 0;
    width: 486px;
    height: 530px;
  }
  .wordmark {
    position: absolute;
    top: 44px;
    left: 0;
    right: 0;
    margin: 0;
    font-size: 118px;
    font-weight: 600;
    line-height: 130px;
    letter-spacing: 2px;
    color: var(--white);
  }
  .headline {
    position: absolute;
    top: 240px;
    left: 0;
    right: 0;
    margin: 0;
    font-weight: 800;
    font-size: 42px;
    line-height: 45px;
    text-transform: uppercase;
  }
  .headline__dark { color: var(--ink); display: block; }
  .headline__lime { color: var(--lime); display: block; }
  .headline__light { color: var(--white); display: block; }
  .divider {
    position: absolute;
    top: 398px;
    left: 70px;
    width: 347px;
    height: 2px;
    background: var(--white);
  }
  .standard-name {
    position: absolute;
    top: 410px;
    left: 40px;
    right: 40px;
    margin: 0;
    font-size: 25px;
    font-weight: 600;
    line-height: 31px;
    text-transform: uppercase;
  }
  .tagline {
    position: absolute;
    top: 530px;
    left: 10px;
    right: 10px;
    margin: 0;
    font-size: 25px;
    font-weight: 600;
    line-height: 31px;
  }
  .globe-visual {
    position: absolute;
    top: 630px;
    left: 20px;
    width: 446px;
    height: 400px;
    border-radius: 50%;
    background: radial-gradient(circle at 50% 55%, var(--globe) 0%, rgba(26,29,74,.45) 55%, rgba(11,10,29,0) 72%);
  }
  .qr-frame {
    position: absolute;
    top: 745px;
    left: 158px;
    width: 164px;
    height: 164px;
    box-sizing: border-box;
    border: 4px solid var(--lime);
    border-radius: 12px;
    background: var(--white);
  }
  .contact {
    position: absolute;
    left: 0;
    right: 0;
    margin: 0;
    font-size: 22px;
    font-weight: 700;
    line-height: 26px;
    text-transform: uppercase;
  }
  .contact--email { top: 1041px; color: var(--lime); }
  .contact--web { top: 1081px; color: var(--link); }
</style>
</head>
<body>
  <main class="banner">
    <svg class="banner__header" viewBox="0 0 486 530" aria-hidden="true">
      <defs>
        <linearGradient id="header-fade" x1="0" y1="0" x2="0" y2="1">
          <stop offset="0" stop-color="var(--green)"/>
          <stop offset="0.55" stop-color="var(--teal)"/>
          <stop offset="1" stop-color="var(--blue)"/>
        </linearGradient>
      </defs>
      <path d="M0 0 H486 V410 Q243 622 0 410 Z" fill="var(--lime)"/>
      <path d="M0 0 H486 V392 Q243 614 0 392 Z" fill="var(--white)"/>
      <path d="M0 0 H486 V385 Q243 607 0 385 Z" fill="url(#header-fade)"/>
    </svg>

    <p class="wordmark">csln</p>

    <h1 class="headline">
      <span class="headline__dark">Mapping the</span>
      <span class="headline__lime">World's Internet</span>
      <span class="headline__light">Backbone.</span>
    </h1>

    <div class="divider"></div>
    <p class="standard-name">Civic Strand<br>Ledger Norm</p>

    <p class="tagline">A community-driven solution<br>for mapping the world's<br>Internet backbone</p>

    <div class="globe-visual" role="img" aria-label="Faint dotted network globe with glowing connection points"></div>

    <div class="qr-frame" role="img" aria-label="Space reserved for the mailing-list QR code"></div>

    <p class="contact contact--email">outreach@cslnorm.net</p>
    <p class="contact contact--web">www.cslnorm.net</p>
  </main>
</body>
</html>
```